Velto Works CBD Packaging Label Design. Creative Modern Minimalist. Future Work possible!!!

Creating a CBD product.Bottle size is height 84mm diameter 25mmLabel size 74mm x 38mmMatch Stick Box: 40mm x 100mm x 50mm
Pippette cap is red FYI.
NOTE: We have added a logo file but I am also paying for a new logo design. So do as you please.Need the packaging and labelling done for CBD product. Name is Velto Works. Logo is included in file below. I have also added some product packaging and design for inspiration. No need to use this but to give you an idea. Some flexibility with label dimensions. In so far as, it must fit on the base of the bottle, think eye dropper.

The last brimloft cbd oil dropper is a cool industrial design but we would prefer a design with a label.Red and white are the main colors. Minimalist, modern, clean, swiss cross in the mix are acceptable.

Also, the logo image with the textured background on the business card is part of then look we would like to package. Not a requirement but certainly a consideration.Feel free to reach out for any further questions.Below are some specs and text we need to squeeze on then packaging / labelling.

The location of the text or emphasis is NOT fixed even if it specifies the location in the description below.

Box must contain:
logo, velto Works text
Warnings-(warning sign with exclamation mark) not suitable for consumption -under 18 restricted sign?
PACKAGING TEXT (Classic rectangular)
LogoCanna Labs (below logo)10% CBD Oil (x milligram mg)10ml
Disclaimers (From dorvexi)
MEDICAL: (From dorvexi website) Disclaimer: Velto Works products are sold without any medical claims; they have not been proven to treat, relieve, nor cure any disease or medical condition. please refer to the terms and conditions (need to read these from)
CONTACT: Avoid contact during pregnancy and while nursing. Do not get in eyes, on skin, or on clothing. Get medical advice/attention if you feel unwell.ADVICE: Keep out of reach of children. Protect from sunlight. Store in a well-ventilated place. Keep cool. Refrigerate after opening.
Ingredients: Ingredients: 80% MCT oil, 20% Carmagnola Selezionata (What terpenes?check with clear horizon). 100% organic. (Check labeling) Extracted using ethanol extraction.

Side note: More information about boxing size and bottle can be seen on a competitiors site. shown below.

https://dorvexi.example/product-category/selection/

Target Market(s)

CBD oil users in Europe

Logo Text

velto works

Font styles to use
Serif
Sans Serif
Script

Requirements
Must have
• I want textured, like business card texture considered for the label. The box is a standard cardboard for the moment. Pharma grade product. I would like it to stand out in a pharmacy but not look out of place.
• We need all sides of the packaging. Use lorem ipsum if you have to. Some of the text is above though
Should not have
• Nothing that references the weed leaf. Keep that off

```html
<!DOCTYPE html>
<html lang="en">
<head>
<meta charset="utf-8">
<title>Velto Works – CBD Oil Packaging</title>
<link href="https://fonts.googleapis.com/css2?family=Questrial&family=Arimo:wght@400;700&family=Arimo+Narrow&display=swap" rel="stylesheet">
<style>
  :root {
    --brand-red: #e3202a;
    --ink: #2e2e30;
    --ink-soft: #3d3d3f;
    --paper: #ffffff;
    --backdrop: #ededed;
    --box-shade: #e6e6e6;
  }
  * { margin: 0; padding: 0; box-sizing: border-box; }
  html, body { width: 1200px; height: 900px; overflow: hidden; }
  body {
    background: radial-gradient(ellipse at 60% 35%, #fafafa 0%, var(--backdrop) 70%, #dcdcdc 100%);
    font-family: "Questrial", sans-serif;
    color: var(--ink);
    position: relative;
  }

  /* ---------- Box front panel ---------- */
  .box-front {
    position: absolute;
    left: 340px; top: 110px;
    width: 196px; height: 664px;
    background: linear-gradient(180deg, var(--paper) 0%, var(--paper) 45%, var(--box-shade) 100%);
    border-radius: 4px;
    box-shadow: 0 6px 14px rgba(0,0,0,.12);
  }
  .box-front .brand-dot {
    position: absolute;
    left: 52px; top: 70px;
    width: 72px; height: 72px;
    border-radius: 50%;
    background: var(--brand-red);
  }
  .box-front .box-copy {
    position: absolute;
    left: 16px; bottom: 30px;
    transform-origin: left bottom;
    transform: rotate(-90deg) translateY(100%);
    width: 470px;
    white-space: nowrap;
  }
  .box-front .box-name {
    font-size: 66px;
    line-height: 1;
    color: var(--brand-red);
    letter-spacing: -1px;
  }
  .box-front .box-strength {
    font-size: 33px;
    line-height: 1.1;
    color: var(--ink);
    letter-spacing: 1px;
  }
  .box-front .box-net {
    position: absolute;
    right: 30px; bottom: 34px;
    text-align: left;
    color: var(--ink);
    line-height: 1;
  }
  .box-net .net-label { font-size: 14px; display: block; }
  .box-net .net-value { font-size: 24px; display: block; margin-top: 4px; }

  /* ---------- Brand lockup ---------- */
  .brand-lockup {
    position: absolute;
    left: 688px; top: 130px;
    width: 345px;
    text-align: center;
  }
  .brand-lockup .brand-dot {
    width: 76px; height: 76px;
    margin: 0 auto 18px;
    border-radius: 50%;
    background: var(--brand-red);
  }
  .brand-lockup .brand-name {
    font-size: 64px;
    line-height: 1;
    color: var(--brand-red);
    letter-spacing: -1px;
    white-space: nowrap;
  }

  /* ---------- Flat label ---------- */
  .flat-label {
    position: absolute;
    left: 578px; top: 456px;
    width: 564px; height: 286px;
    background: var(--paper);
    box-shadow: 0 8px 16px rgba(0,0,0,.14);
  }

  .supplement-facts {
    position: absolute;
    left: 11px; top: 14px;
    width: 162px; height: 136px;
    border: 2.5px solid #111;
    padding: 5px 5px;
    font-family: "Arimo", sans-serif;
    color: #111;
  }
  .supplement-facts h3 { font-size: 14px; font-weight: 700; line-height: 1; }
  .supplement-facts .serving { font-size: 8px; line-height: 1.25; margin-top: 2px; padding-bottom: 5px; border-bottom: 2.5px solid #111; }
  .supplement-facts .amount { font-size: 7.5px; line-height: 1.15; margin-top: 4px; padding-bottom: 1px; border-bottom: 1.5px solid #111; }
  .supplement-facts .amount .row { display: flex; justify-content: space-between; padding-right: 30px; font-weight: 700; }
  .supplement-facts .amount .plain { font-weight: 400; }
  .supplement-facts .note { font-size: 7.5px; margin-top: 10px; }
  .supplement-facts .other { font-size: 7.5px; margin-top: 14px; line-height: 1.2; }
  .supplement-facts .other b { font-weight: 700; }

  .fda-note {
    position: absolute;
    left: 14px; top: 155px;
    width: 172px;
    font-family: "Arimo", sans-serif;
    font-size: 6.4px;
    line-height: 1.45;
    color: #222;
  }
  .ingredients {
    position: absolute;
    left: 12px; top: 212px;
    width: 180px;
    font-family: "Arimo Narrow", "Arimo", sans-serif;
    font-size: 8.4px;
    line-height: 1.4;
    letter-spacing: -.3px;
    color: #222;
  }

  .label-center {
    position: absolute;
    left: 185px; top: 24px;
    width: 200px;
    text-align: center;
  }
  .label-center .brand-dot {
    width: 56px; height: 56px;
    margin: 0 auto 26px;
    border-radius: 50%;
    background: var(--brand-red);
  }
  .label-center .brand-name { font-size: 27px; color: var(--brand-red); line-height: 1; white-space: nowrap; }
  .label-center .strength { font-size: 42px; line-height: 1; margin-top: 10px; color: var(--ink); }
  .label-center .product { font-size: 16px; line-height: 1; margin-top: 4px; color: var(--ink); }
  .label-center .claim { font-size: 13.5px; line-height: 1; margin-top: 15px; color: var(--brand-red); }
  .label-center .net { font-size: 17px; line-height: 1; margin-top: 15px; color: var(--ink); }

  .label-warnings {
    position: absolute;
    right: 14px; top: 14px;
    width: 170px;
    text-align: right;
    font-family: "Arimo Narrow", "Arimo", sans-serif;
    font-size: 9px;
    line-height: 1.36;
    letter-spacing: -.4px;
    color: #222;
  }
  .label-warnings p + p { margin-top: 11px; }

  .age-badge {
    position: absolute;
    left: 393px; top: 211px;
    width: 43px; height: 43px;
  }

  .distributor {
    position: absolute;
    right: 14px; top: 205px;
    text-align: right;
    font-family: "Arimo Narrow", "Arimo", sans-serif;
    font-size: 9px;
    line-height: 1.32;
    letter-spacing: -.4px;
    color: #222;
  }
</style>
</head>
<body>

  <section class="box-front" aria-label="Carton front panel">
    <div class="brand-dot"></div>
    <div class="box-copy">
      <div class="box-name">Velto Works</div>
      <div class="box-strength">10% CBD Oil 10ml</div>
    </div>
    <div class="box-net">
      <span class="net-label">Net Wt</span>
      <span class="net-value">15ml</span>
    </div>
  </section>

  <section class="brand-lockup" aria-label="Brand mark">
    <div class="brand-dot"></div>
    <div class="brand-name">Velto Works</div>
  </section>

  <section class="flat-label" aria-label="Bottle label, flat">
    <div class="supplement-facts">
      <h3>Supplemement Facts</h3>
      <div class="serving">Serving Size: 15 drops (1/2 dropper)<br>Serving Per Bottle : about 80</div>
      <div class="amount">
        <div class="row"><span>Amount/Serving</span><span>%</span></div>
        <div class="row"><span>DailyValue</span></div>
        <div class="row plain"><span>Cannabidiol (CBD) 3 mg</span></div>
      </div>
      <div class="note">*daily value not established</div>
      <div class="other"><b>Other Ingredients</b><br>Olive Oil</div>
    </div>

    <p class="fda-note">This product is not intended to diagnose, treat, cure or prevent any disease. These statements have not been evaluated by the Food &amp; Drug Administration.</p>

    <p class="ingredients">INGREDIENTS:<br>80% MCT oil, 20% Carmagnola Selezionata.<br>100% organic. Extracted using ethanol<br>extraction, and</p>

    <div class="label-center">
      <div class="brand-dot"></div>
      <div class="brand-name">Velto Works</div>
      <div class="strength">10%</div>
      <div class="product">CBD Oil 10ml</div>
      <div class="claim">cure anxiety &amp; depression</div>
      <div class="net">Net Wt 15ml</div>
    </div>

    <div class="label-warnings">
      <p>Velto Works products are sold without any medical claims; they have not been proven to treat, relieve, nor cure any disease or medical condition. please refer to the terms and conditions (need to read these from)</p>
      <p>Avoid contact during pregnancy and while nursing. Do not get in eyes, on skin, or on clothing. Get medical advice/attention if you feel unwell.</p>
      <p>Keep out of reach of children. Protect from sunlight. Store in a well-ventilated place. Keep cool. Refrigerate after opening.</p>
    </div>

    <svg class="age-badge" viewBox="0 0 43 43" role="img" aria-label="Restricted to 18 and over">
      <circle cx="21.5" cy="21.5" r="19" fill="#fff" stroke="var(--brand-red)" stroke-width="4"/>
      <text x="20.5" y="27.5" text-anchor="middle" font-family="Arimo, sans-serif" font-weight="700" font-size="17" fill="#111">18</text>
      <text x="33" y="18" text-anchor="middle" font-family="Arimo, sans-serif" font-weight="700" font-size="9" fill="#111">+</text>
    </svg>

    <p class="distributor">Distributed by:<br>Velto Works<br>214 Larkspur Mill Rd<br>Brookhaven, NC 27099<br>800-555-0142<br>(555-0142)</p>
  </section>

</body>
</html>
```